Real estate business needing a creative mind!

Have a real estate business called Brightwell Estates LLC. I need some business card with custom logo. That logo can be an intricate design of a house or houses. Maybe some blue and orange colors, maybe the business name in orange. Some thing that leaves a wow impression to the holder. Or just surprise me! Must have business name, name, email and phone number.

Target Market(s)

Property sellers and real estate professionals

Industry/Entity Type

Real estate

Contact Information for Business Card

Want it to stand out but also be professional.

Colors

Designer to choose colors to be used in the design.

Requirements
Must have
• Business name Brightwell Estates. My name which is Dalton Meese. The business email which is Brightwellestates1@novamail.example. The phone number which is 555-014-2297
Nice to have
• Could be a logo of the name over some mountain houses being that we live by the Smokey mountains. Could have a sun if it looks ok?

```html
<!DOCTYPE html>
<html lang="en">
<head>
<meta charset="utf-8">
<title>Brightwell Estates – Business Card</title>
<link rel="stylesheet" href="https://fonts.googleapis.com/css2?family=Montserrat:wght@400;500;700&display=swap">
<style>
  :root {
    --navy: #2a2a8c;
    --orange: #f0942a;
    --paper: #ffffff;
    --backdrop: #e9e9ec;
    --ink: #2a2a8c;
  }
  * { box-sizing: border-box; margin: 0; padding: 0; }
  html, body { width: 1200px; height: 787px; overflow: hidden; }
  body {
    background: var(--backdrop);
    font-family: "Montserrat", sans-serif;
    position: relative;
  }
  .card {
    position: absolute;
    top: 239px;
    width: 540px;
    height: 309px;
    overflow: hidden;
    box-shadow: 0 10px 28px rgba(0,0,0,0.18);
  }
  .card--front { left: 40px; background: var(--paper); }
  .card--back { left: 620px; background: var(--navy); }

  .brand {
    position: absolute;
    display: flex;
    align-items: center;
    gap: 10px;
    font-weight: 700;
    letter-spacing: 0.5px;
  }
  .brand__dot {
    width: 18px; height: 18px; border-radius: 50%;
    background: var(--orange);
  }
  .card--front .brand { left: 120px; top: 62px; font-size: 30px; color: var(--navy); }
  .card--back .brand {
    left: 0; right: 0; top: 128px; justify-content: center;
    font-size: 36px; color: #fff;
  }
  .brand__rule {
    position: absolute; height: 2px; background: var(--orange);
  }
  .card--front .brand__rule { left: 120px; top: 112px; width: 290px; }
  .card--back .brand__rule { left: 110px; top: 186px; width: 320px; }

  .accent-line {
    position: absolute; left: 0; top: 196px;
    width: 238px; height: 7px; background: var(--orange);
  }
  .footer-band {
    position: absolute; left: 238px; top: 258px;
    width: 302px; height: 51px; background: var(--navy);
    border-top-left-radius: 26px;
  }
  .side-tab {
    position: absolute; right: 0; top: 210px;
    width: 20px; height: 30px; background: var(--navy);
    border-top-left-radius: 12px;
  }

  .contact {
    position: absolute; display: flex; align-items: center; gap: 8px;
    color: var(--ink); font-size: 13px; font-weight: 500;
  }
  .contact svg { flex: none; }
  .contact--phone { left: 76px; top: 146px; }
  .contact--email { left: 220px; top: 222px; font-size: 12.5px; }

  .holder-name {
    position: absolute; right: 40px; top: 138px;
    color: var(--orange); font-weight: 700; font-size: 24px;
    letter-spacing: 0.5px; text-transform: uppercase;
  }
</style>
</head>
<body>
  <section class="card card--front">
    <div class="brand"><span class="brand__dot"></span>Brightwell Estates</div>
    <div class="brand__rule"></div>

    <div class="contact contact--phone">
      <svg width="14" height="14" viewBox="0 0 24 24" aria-hidden="true">
        <path fill="var(--orange)" d="M6.6 10.8a15.1 15.1 0 0 0 6.6 6.6l2.2-2.2a1 1 0 0 1 1-.25 11.4 11.4 0 0 0 3.6.57 1 1 0 0 1 1 1V20a1 1 0 0 1-1 1A17 17 0 0 1 3 4a1 1 0 0 1 1-1h3.5a1 1 0 0 1 1 1c0 1.25.2 2.45.57 3.6a1 1 0 0 1-.25 1z"/>
      </svg>
      <span>555-014-2297</span>
    </div>

    <div class="holder-name">Dalton Meese</div>

    <div class="accent-line"></div>

    <div class="contact contact--email">
      <span>Brightwellestates1@novamail.example</span>
      <svg width="15" height="15" viewBox="0 0 24 24" aria-hidden="true" fill="none" stroke="var(--orange)" stroke-width="2">
        <circle cx="12" cy="12" r="9"/>
        <path d="M3 12h18M12 3c3 3.2 3 14.8 0 18M12 3c-3 3.2-3 14.8 0 18"/>
      </svg>
    </div>

    <div class="side-tab"></div>
    <div class="footer-band"></div>
  </section>

  <section class="card card--back">
    <div class="brand"><span class="brand__dot"></span>Brightwell Estates</div>
    <div class="brand__rule"></div>
  </section>
</body>
</html>
```